Business Card Design Project

The logo I included in my order was a previous image that we've used for shirts, signs, magnets, etc. We've decided to go back to that logo, with some updates.
We need to add "Inc." after "Brindel Roofing,"
Also, I need the logo with a transparent background so that I can use it on other projects.

The business cards will be the first item I order with the new logo. The employee's info is:
Derek Pallow
Sales Manager
484-611-3907
dpallow@brindelroofinginc.example

Also, I want a "Find us on Linkora" icon on the card, along with our web address, www.brindelroofinginc.example.

Any questions, please email or call me:
norabrindel@mailbox.example
484-290-6153

Reason: This is the first time I've tried Pixel Forum.

My timetable changed and I need to select a design by the end of the work day, 6 hours from now.Thanks so much for all of the super designs.

Target Market(s)

Homeowners

Industry/Entity Type

Business

Font styles to use
Serif

Requirements
Must have
• Transparent background
Similar to logo in photo I sent you

```html
<!DOCTYPE html>
<html lang="en">
<head>
<meta charset="utf-8">
<title>Brindel Roofing – Business Card</title>
<link rel="stylesheet" href="https://fonts.googleapis.com/css2?family=Lato:wght@300;400;700&display=swap">
<style>
  :root {
    --backdrop: #2a2a2a;
    --card: #9b9b9b;
    --ink: #111111;
    --ink-soft: #222222;
    --band: #3f5aa8;
    --band-text: #ffffff;
    --social: #3b5998;
  }
  * { box-sizing: border-box; margin: 0; padding: 0; }
  html, body {
    width: 1200px; height: 899px; overflow: hidden;
    background: var(--backdrop);
    font-family: "Lato", Arial, sans-serif;
  }
  .card {
    position: absolute; left: 240px; top: 244px;
    width: 720px; height: 411px;
    background: var(--card);
    color: var(--ink);
  }
  .brand {
    position: absolute; left: 40px; top: 70px; width: 320px;
    display: flex; align-items: center; gap: 12px;
  }
  .brand-mark { width: 26px; height: 26px; background: var(--ink); flex: none; }
  .brand-name { font-size: 34px; font-weight: 700; color: var(--ink); white-space: nowrap; }
  .main-phone {
    position: absolute; left: 40px; top: 150px; width: 340px; text-align: center;
    font-size: 33px; font-weight: 400; color: var(--ink-soft);
  }
  .services {
    position: absolute; left: 20px; top: 198px; width: 380px; text-align: center;
    font-size: 21px; color: var(--ink-soft);
  }
  .person { position: absolute; right: 22px; top: 62px; text-align: right; }
  .person-name { font-size: 30px; font-weight: 300; letter-spacing: 0.5px; text-transform: uppercase; }
  .person-name b { font-weight: 700; }
  .person-title { font-size: 17px; color: var(--ink-soft); margin-top: 2px; }
  .person-phone { font-size: 27px; margin-top: 34px; }
  .social {
    display: flex; align-items: center; justify-content: flex-end; gap: 10px; margin-top: 12px;
  }
  .social-square { width: 40px; height: 40px; background: var(--social); }
  .social-text { text-align: left; color: var(--social); line-height: 1.05; }
  .social-text small { display: block; font-size: 12px; }
  .social-text span { font-size: 22px; }
  .band {
    position: absolute; left: 0; right: 0; top: 292px; height: 78px;
    background: var(--band); color: var(--band-text);
    display: flex; justify-content: space-between; align-items: center;
    padding: 0 22px 0 30px;
  }
  .address { font-size: 22px; line-height: 1.3; }
  .web { font-size: 17px; line-height: 1.35; text-align: right; }
</style>
</head>
<body>
  <main class="card">
    <div class="brand">
      <span class="brand-mark"></span>
      <span class="brand-name">Brindel Roofing</span>
    </div>
    <p class="main-phone">610-358-2241</p>
    <p class="services">Roofing - Siding - Seamless Gutters</p>

    <section class="person">
      <p class="person-name">Derek <b>Pallow</b></p>
      <p class="person-title">Sales Manager</p>
      <p class="person-phone">484-611-3907</p>
      <div class="social">
        <span class="social-square"></span>
        <p class="social-text"><small>Find us on</small><span>Linkora</span></p>
      </div>
    </section>

    <footer class="band">
      <p class="address">482 Ridgecrest Lane<br>Hollowbrook, Pa 18230</p>
      <p class="web">dpallow@brindelroofinginc.example<br>www.brindelroofinginc.example</p>
    </footer>
  </main>
</body>
</html>
```